Brightvane Group Word Press Website

We need a graphical, fun website that conveys our messaging of providing the Top-Tier Keystone Outreach Program for Mortgage Loan Officers and Realtors. Our system uses AI and Predictive Analysis to uncover the 'Gold' hidden in contact databases. The 'Gold' is defined as people who are in the market or likely to be in the market soon. We place that 'Gold' in the form of Contact Name, Address, Phone and Email on a Daily To Do List detailing what type of contact should be made.

Target Market(s)

Mortgage Loan Officers and Realtors

Industry/Entity Type

Mortgage & Real Estate

Coding

Coded - Design and coding required

Number of Pages Required

5+ page

Requirements
Must have
• I like the look of this site- https://www.hearthloanstudio.example/
Nice to have
• Please create a flow that is similar to https://www.hearthloanstudio.example/, but better, more dynamic. Site must be responsive and mobile friendly. Site will have embedded videos. Site need to convey a message of hope, imagination, innovation, results oriented, better than the rest, victory!
Should not have
• Nothing cheesy or low class.

```html
<!DOCTYPE html>
<html lang="en">
<head>
<meta charset="utf-8">
<title>Brightvane Group — Marketing for Mortgage Loan Officers and Realtors</title>
<link href="https://fonts.googleapis.com/css2?family=Poppins:wght@400;500;600;700&display=swap" rel="stylesheet">
<style>
:root{
  --blue:#1a93d6;
  --blue-deep:#0d66a6;
  --blue-dark:#0a5a96;
  --gold:#f0c53a;
  --gold-deep:#dcab1f;
  --ink:#1c1c2a;
  --text:#3b3b48;
  --muted:#f3f2f8;
  --white:#ffffff;
}
*{box-sizing:border-box;margin:0;padding:0}
html,body{width:1200px;height:3787px;overflow:hidden}
body{position:relative;font-family:"Poppins",sans-serif;color:var(--text);background:var(--white)}
.abs{position:absolute}
.btn{position:absolute;display:flex;align-items:center;justify-content:center;background:linear-gradient(180deg,var(--gold),var(--gold-deep));color:var(--white);font-weight:600;font-size:14px;letter-spacing:3px;text-transform:uppercase;border-radius:3px}
.link-more{position:absolute;color:var(--gold-deep);font-size:13px;font-weight:600;letter-spacing:2.5px;border-bottom:2px solid var(--gold-deep);padding-bottom:2px}
.ph{position:absolute}

/* hero */
.hero{position:absolute;left:0;top:0;width:1200px;height:680px;background:linear-gradient(135deg,var(--blue-deep) 0%,var(--blue) 55%,#22a6e6 100%)}
.topbar{position:absolute;right:0;top:0;width:502px;height:32px;background:var(--gold-deep);clip-path:polygon(4% 0,100% 0,100% 100%,0 100%);display:flex;align-items:center;justify-content:flex-end;gap:18px;padding-right:150px;color:var(--white);font-size:12px;white-space:nowrap}
.topbar span{display:flex;align-items:center;gap:6px;flex:none}
.brand{position:absolute;display:flex;align-items:center;gap:8px;color:var(--gold);font-weight:700;white-space:nowrap}
.brand .dot{width:14px;height:14px;border-radius:50%;background:var(--gold)}
.nav{position:absolute;top:55px;left:612px;display:flex;gap:42px;color:var(--white);font-size:15px;font-weight:500}
.nav .active{position:relative}
.nav .active::after{content:"";position:absolute;left:50%;top:26px;width:6px;height:6px;margin-left:-3px;border-radius:50%;background:var(--gold)}
.hero-kicker{position:absolute;top:178px;left:0;width:1200px;text-align:center;color:var(--white);font-size:22px;font-weight:500}
.hero-title{position:absolute;top:205px;left:0;width:1200px;text-align:center;color:var(--white);font-size:54px;font-weight:700;line-height:62px}
.scroll{position:absolute;left:587px;top:463px;width:26px;height:42px;border:3px solid var(--white);border-radius:14px}
.scroll::after{content:"";position:absolute;left:8px;top:8px;width:4px;height:10px;border-radius:2px;background:var(--white)}
.scroll-label{position:absolute;top:516px;left:0;width:1200px;text-align:center;color:var(--white);font-size:12px;letter-spacing:3px;font-weight:500}

/* about */
.sec-small{font-size:31px;color:var(--ink);font-weight:500}
.sec-title{font-size:53px;color:var(--ink);font-weight:700;line-height:1.1;white-space:nowrap}
.body-copy{font-size:15px;line-height:27px;color:var(--text)}

/* services */
.services{position:absolute;left:0;top:1188px;width:1200px;height:500px;background:var(--muted)}
.service{position:absolute;top:162px;width:210px;margin-left:-105px;text-align:center}
.service .icon{width:94px;height:94px;margin:0 auto;border-radius:12px;display:flex;align-items:center;justify-content:center}
.service h3{margin-top:20px;font-size:15px;font-weight:600;color:var(--ink);white-space:nowrap}
.service p{margin-top:6px;font-size:14px;line-height:23px;color:var(--text)}
.service .link-more{position:relative;display:inline-block;margin-top:8px}

/* gold features */
.features{position:absolute;left:0;top:1688px;width:1200px;height:600px;background:linear-gradient(120deg,var(--blue-dark) 0%,var(--blue) 60%,#2aa7e4 100%)}
.feature{position:absolute;display:flex;align-items:center;gap:14px;color:var(--white);font-size:15px;font-weight:600;white-space:nowrap}

/* recent work */
.ticks li{list-style:none;position:relative;padding-left:20px;font-size:14.5px;line-height:22px;color:var(--ink);margin-bottom:12px}
.ticks svg{position:absolute;left:0;top:5px}

/* blog */
.blog{position:absolute;left:0;top:2794px;width:1200px;height:640px;background:var(--muted)}
.card{position:absolute;top:122px;width:269px}
.card .img{height:183px;border-radius:2px}
.card .date{margin-top:12px;font-size:11.5px;color:var(--blue-deep);font-weight:500}
.card h4{margin-top:2px;font-size:17px;font-weight:600;color:var(--ink)}
.card p{margin-top:8px;font-size:14px;line-height:21px;color:var(--text)}
.card .link-more{position:relative;display:inline-block;margin-top:16px}
.arrow{position:absolute;top:2997px;width:38px;height:38px;border-radius:50%;display:flex;align-items:center;justify-content:center}

/* footer */
.footer{position:absolute;left:0;top:3420px;width:1200px;height:367px;background:linear-gradient(120deg,var(--blue-dark),var(--blue) 70%)}
.contact{position:absolute;left:187px;display:flex;align-items:center;gap:12px;color:var(--white);font-size:15px;line-height:23px;white-space:nowrap}
.contact .ci{width:46px;height:46px;border-radius:50%;background:var(--gold);display:flex;align-items:center;justify-content:center;flex:none}
.subscribe-title{position:absolute;left:760px;top:3470px;color:var(--white);font-size:25px;font-weight:600;line-height:27px}
.email-field{position:absolute;left:762px;top:3538px;width:264px;height:40px;background:var(--white);border-radius:2px;display:flex;align-items:center;gap:6px;padding-left:12px;font-size:12px;color:#8a8a96}
.bottombar{position:absolute;left:0;top:3731px;width:1200px;height:56px;background:var(--blue-dark)}
.copy{position:absolute;left:172px;top:18px;color:var(--white);font-size:13px}
.copy b{color:var(--gold);font-weight:400}
.social{position:absolute;top:12px;width:29px;height:29px;border-radius:50%;background:var(--gold)}
</style>
</head>
<body>

<!-- Hero -->
<header class="hero">
  <div class="topbar">
    <span><svg width="12" height="12" viewBox="0 0 24 24" fill="#fff"><path d="M6.6 10.8a15 15 0 0 0 6.6 6.6l2.2-2.2c.3-.3.7-.4 1-.2 1.1.4 2.3.6 3.6.6.6 0 1 .4 1 1V20c0 .6-.4 1-1 1A17 17 0 0 1 3 4c0-.6.4-1 1-1h3.5c.6 0 1 .4 1 1 0 1.3.2 2.5.6 3.6.1.3 0 .7-.2 1z"/></svg>01 555 014 277</span>
    <span><svg width="13" height="10" viewBox="0 0 24 18"><path d="M1 1h22v16H1z" fill="none" stroke="#fff" stroke-width="2"/><path d="M1 1l11 9 11-9" fill="none" stroke="#fff" stroke-width="2"/></svg>info@brightvanegroup.example</span>
  </div>
  <div class="brand" style="left:150px;top:58px;font-size:24px"><span class="dot"></span>Brightvane Group</div>
  <nav class="nav">
    <span class="active">Home</span><span>Services</span><span>About</span><span>Blog</span><span>Contact</span>
  </nav>
  <div class="hero-kicker">Top-Tier Keystone Outreach Program for</div>
  <h1 class="hero-title">Mortgage Loan Officers<br>and Realtors</h1>
  <div class="btn" style="left:515px;top:353px;width:170px;height:42px">Know More</div>
  <div class="scroll"></div>
  <div class="scroll-label">SCROLLDOWN</div>
</header>
<svg class="abs" style="left:0;top:540px" width="1200" height="145" viewBox="0 0 1200 145" preserveAspectRatio="none">
  <path d="M0 139 Q600 -87 1200 139 L1200 145 L0 145Z" fill="#fff"/>
  <path d="M0 129 Q600 -97 1200 129" fill="none" stroke="var(--gold)" stroke-width="5"/>
</svg>

<!-- About -->
<section>
  <div class="abs sec-small" style="left:172px;top:690px">About</div>
  <h2 class="abs sec-title" style="left:172px;top:732px;font-size:46px">Brightvane Group</h2>
  <p class="abs body-copy" style="left:172px;top:810px;width:370px">Lorem ipsum dolor sit amet, consetur adipiscing elit. Integer suscipit in leo in semper. Nunc sed metus malesuada, rutrum erat non, eleifend est. Aenean sit amet viverra metus, sed tincidunt leo. Fusce pretium nunc risus, et sodales quam tincidunt porta.</p>
  <div class="btn" style="left:169px;top:996px;width:172px;height:44px">Read More</div>
  <div class="ph" role="img" aria-label="Laptop and phone showing an analytics dashboard" style="left:660px;top:675px;width:440px;height:485px;border-radius:18px;background:linear-gradient(160deg,#ecebea 0%,#dcd9d7 60%,#c94a68 100%);opacity:.9"></div>
</section>

<!-- Services -->
<section class="services">
  <h2 class="abs sec-title" style="left:0;top:56px;width:1200px;text-align:center">Our Services</h2>
  <div class="service" style="left:268px">
    <div class="icon" style="background:#bfe9f8"><svg width="46" height="40" viewBox="0 0 46 40"><rect x="2" y="2" width="30" height="22" rx="4" fill="#1c9ad8"/><rect x="16" y="14" width="28" height="20" rx="4" fill="#5fc3ee"/><path d="M10 24l-4 8 10-8z" fill="#1c9ad8"/></svg></div>
    <h3>Mortgage Chatbot</h3><p>Maecenas arcu ri posuere ac lacus vitae</p><span class="link-more">READ MORE</span>
  </div>
  <div class="service" style="left:490px">
    <div class="icon" style="background:#fbdcc0"><svg width="40" height="40" viewBox="0 0 40 40"><circle cx="20" cy="13" r="8" fill="#e99b52"/><path d="M5 36c0-9 7-13 15-13s15 4 15 13z" fill="#e99b52"/></svg></div>
    <h3>Reputation Management</h3><p>Maecenas arcu ri posuere ac lacus vitae</p><span class="link-more">READ MORE</span>
  </div>
  <div class="service" style="left:710px">
    <div class="icon" style="background:#f9d0e2"><svg width="42" height="36" viewBox="0 0 42 36"><path d="M4 12h8l20-9v28l-20-9H4z" fill="#e8467e"/><rect x="10" y="21" width="6" height="11" fill="#e8467e"/><circle cx="36" cy="17" r="3" fill="#e8467e"/></svg></div>
    <h3>Marketing</h3><p>Maecenas arcu ri posuere ac lacus vitae</p><span class="link-more">READ MORE</span>
  </div>
  <div class="service" style="left:932px">
    <div class="icon" style="background:#d3f1cf"><svg width="40" height="42" viewBox="0 0 40 42"><circle cx="14" cy="9" r="6" fill="#49b54a"/><path d="M4 40V24c0-5 4-8 10-8s10 3 10 8v16z" fill="#49b54a"/><rect x="26" y="14" width="10" height="12" fill="#49b54a"/></svg></div>
    <h3>Realtors</h3><p>Maecenas arcu ri posuere ac lacus vitae</p><span class="link-more">READ MORE</span>
  </div>
  <div class="btn" style="left:532px;top:419px;width:134px;height:43px">View All</div>
</section>

<!-- Gold features -->
<section class="features">
  <div class="ph" role="img" aria-label="Phone showing two colleagues reviewing documents" style="left:256px;top:28px;width:210px;height:441px;border-radius:22px;border:6px solid #e9ecef;background:linear-gradient(180deg,#dfe5ea,#8f9aa6)"></div>
  <h2 class="abs" style="left:590px;top:50px;color:#fff;font-size:52px;font-weight:700;line-height:52px">Our Gold<br>Features</h2>
  <p class="abs" style="left:590px;top:168px;width:425px;color:#fff;font-size:14.5px;line-height:23px">Lorem ipsum dolor sit amet, consetur ading elit. Integer suscipit in leo in semper. Nunc sed metus malesuada, rutrum erat non, eleifend est. tincidunt porta.</p>
  <div class="feature" style="left:587px;top:260px"><svg width="46" height="46" viewBox="0 0 46 46" fill="none" stroke="#fff" stroke-width="2"><rect x="4" y="4" width="26" height="36" rx="2"/><path d="M10 14h14M10 22h14M10 30h8M32 36l10-14"/></svg>Aenean sollicitudin</div>
  <div class="feature" style="left:825px;top:260px"><svg width="46" height="46" viewBox="0 0 46 46" fill="none" stroke="#fff" stroke-width="2"><rect x="10" y="3" width="26" height="40" rx="4"/><path d="M16 14h14M16 22h14M16 30h14"/></svg>Aenean sollicitudin</div>
  <div class="feature" style="left:587px;top:340px"><svg width="46" height="46" viewBox="0 0 46 46" fill="none" stroke="#fff" stroke-width="2"><circle cx="30" cy="18" r="9"/><rect x="4" y="28" width="22" height="14"/><path d="M8 28v-8h14v8"/></svg>Fusce vulputate</div>
  <div class="feature" style="left:825px;top:340px"><svg width="46" height="46" viewBox="0 0 46 46" fill="none" stroke="#fff" stroke-width="2"><path d="M4 34h10l8 4 18-8M14 34v-6h8l8 4"/><circle cx="28" cy="14" r="6"/></svg>Vivamus fermentum</div>
</section>
<svg class="abs" style="left:0;top:2150px" width="1200" height="150" viewBox="0 0 1200 150" preserveAspectRatio="none">
  <path d="M0 147 Q600 -87 1200 147 L1200 150 L0 150Z" fill="#fff"/>
  <path d="M0 137 Q600 -97 1200 137" fill="none" stroke="var(--gold)" stroke-width="5"/>
</svg>

<!-- Recent work -->
<section>
  <h2 class="abs sec-title" style="left:169px;top:2340px">Recent Work</h2>
  <p class="abs body-copy" style="left:172px;top:2408px;width:350px;font-size:14.5px;line-height:23px">Vestibulum sit amet enim quis est maximus laoreet eu ut nisl. Ut at orci porta, sollicitudin tortor vitae, vehicula nulla.</p>
  <ul class="abs ticks" style="left:172px;top:2500px;width:350px">
    <li><svg width="14" height="12" viewBox="0 0 14 12"><path d="M1 6l4 4 8-9" fill="none" stroke="#49b54a" stroke-width="2.5"/></svg>Vivamus fermentum a leo ut accumsan.</li>
    <li><svg width="14" height="12" viewBox="0 0 14 12"><path d="M1 6l4 4 8-9" fill="none" stroke="#49b54a" stroke-width="2.5"/></svg>Duis vitae neque ut libero imperdiet fringilla vel nec mauris.</li>
    <li><svg width="14" height="12" viewBox="0 0 14 12"><path d="M1 6l4 4 8-9" fill="none" stroke="#49b54a" stroke-width="2.5"/></svg>Quisque mattis nibh sit amet turpis hendrerit, quis vulputate magna ultricies.</li>
  </ul>
  <div class="btn" style="left:172px;top:2662px;width:178px;height:42px">View Project</div>
  <div class="abs" style="left:578px;top:2338px;width:512px;height:346px;border:10px solid #e9e9ec;border-bottom:none;border-radius:8px 8px 0 0;background:#e9e9ec">
    <div class="ph" role="img" aria-label="Team meeting around a table in a glass-walled office" style="left:0;top:0;width:492px;height:336px;background:linear-gradient(180deg,#eef1f3,#b6bcc2)"></div>
  </div>
  <div class="abs" style="left:515px;top:2684px;width:632px;height:12px;border-radius:0 0 10px 10px;background:linear-gradient(180deg,#d6d6d9,#9c9ca2)"></div>
</section>

<!-- Blog -->
<section class="blog">
  <h2 class="abs sec-title" style="left:0;top:30px;width:1200px;text-align:center">Latest Blog</h2>
  <article class="card" style="left:171px">
    <div class="img" role="img" aria-label="Two colleagues working at a laptop" style="background:linear-gradient(180deg,#c9ccd0,#8e949a)"></div>
    <div class="date">Feb 18, 2022</div><h4>Integer vel magna at purus</h4>
    <p>Aliquam diam libero, ultrices sed neque vel, auctor orn mauris. Integer pellentesque bibendum purus,</p>
    <span class="link-more">READ MORE</span>
  </article>
  <article class="card" style="left:465px">
    <div class="img" role="img" aria-label="Team discussing ideas at a wall of sticky notes" style="background:linear-gradient(180deg,#e5e4e1,#9aa0a6)"></div>
    <div class="date">Feb 18, 2022</div><h4>Integer vel magna at purus</h4>
    <p>Aliquam diam libero, ultrices sed neque vel, auctor orn mauris. Integer pellentesque bibendum purus,</p>
    <span class="link-more">READ MORE</span>
  </article>
  <article class="card" style="left:759px">
    <div class="img" role="img" aria-label="Business meeting in a bright office" style="background:linear-gradient(180deg,#eceeef,#a4aab0)"></div>
    <div class="date">Feb 18, 2022</div><h4>Integer vel magna at purus</h4>
    <p>Aliquam diam libero, ultrices sed neque vel, auctor orn mauris. Integer pellentesque bibendum purus,</p>
    <span class="link-more">READ MORE</span>
  </article>
</section>
<div class="arrow" style="left:152px;background:rgba(120,120,130,.55)"><svg width="10" height="16" viewBox="0 0 10 16"><path d="M8 1L2 8l6 7" fill="none" stroke="#fff" stroke-width="2"/></svg></div>
<div class="arrow" style="left:1010px;background:var(--blue)"><svg width="10" height="16" viewBox="0 0 10 16"><path d="M2 1l6 7-6 7" fill="none" stroke="#fff" stroke-width="2"/></svg></div>

<!-- Footer -->
<svg class="abs" style="left:0;top:3290px" width="1200" height="140" viewBox="0 0 1200 140" preserveAspectRatio="none">
  <path d="M0 30 Q600 234 1200 30 L1200 140 L0 140Z" fill="var(--blue-deep)"/>
  <path d="M0 20 Q600 224 1200 20" fill="none" stroke="var(--gold)" stroke-width="5"/>
</svg>
<footer class="footer">
  <div class="contact" style="top:65px"><span class="ci"><svg width="16" height="20" viewBox="0 0 16 20"><path d="M8 0a8 8 0 0 1 8 8c0 6-8 12-8 12S0 14 0 8a8 8 0 0 1 8-8z" fill="#fff"/><circle cx="8" cy="8" r="3" fill="var(--gold)"/></svg></span>12 Harbour Row, Suite 400<br>Northgate, Australia</div>
  <div class="contact" style="top:141px"><span class="ci"><svg width="18" height="14" viewBox="0 0 18 14"><rect width="18" height="14" rx="1" fill="#fff"/><path d="M1 1l8 6 8-6" fill="none" stroke="var(--gold)" stroke-width="1.5"/></svg></span>info@brightvanegroup.example</div>
  <div class="contact" style="top:219px"><span class="ci"><svg width="16" height="16" viewBox="0 0 24 24" fill="#fff"><path d="M6.6 10.8a15 15 0 0 0 6.6 6.6l2.2-2.2c.3-.3.7-.4 1-.2 1.1.4 2.3.6 3.6.6.6 0 1 .4 1 1V20c0 .6-.4 1-1 1A17 17 0 0 1 3 4c0-.6.4-1 1-1h3.5c.6 0 1 .4 1 1 0 1.3.2 2.5.6 3.6.1.3 0 .7-.2 1z"/></svg></span>01 555 014 277</div>
  <div class="brand" style="left:495px;top:150px;width:210px;font-size:24px;flex-direction:column;gap:10px"><span class="dot" style="width:22px;height:22px"></span>Brightvane Group</div>
</footer>
<h3 class="subscribe-title">Subscribe For Latest<br>Update</h3>
<div class="email-field"><svg width="12" height="9" viewBox="0 0 18 14"><rect width="18" height="14" fill="#8a8a96"/><path d="M1 1l8 6 8-6" fill="none" stroke="#fff" stroke-width="1.5"/></svg>Enter email address</div>
<div class="btn" style="left:762px;top:3590px;width:266px;height:40px">Subscribe</div>
<div class="bottombar">
  <div class="copy">© 2022 <b>Brightvane Group</b>. All right reserved</div>
  <span class="social" style="left:923px"></span>
  <span class="social" style="left:961px"></span>
  <span class="social" style="left:998px"></span>
</div>

</body>
</html>
```